Box Design of "pet rapid test for dogs & cats" with professional use

"The market is in Southeast Asia, South America, Europe, and the U.S."
Clients: Veterinary clinics, pet hospitals,(a small number of home use)

Primary colors:
Orange, Green,or Blue, (select 1,or 2 color)
Neutrals: Black, Gray, or White (optional)
Dimensions:135mm(L)*90mm(W)*105mm(W)

Kindly review the attached file for additional content
Updates

I have increased my budget, please provide a satisfactory design solution, thank you very much for your work.

Target Market(s)

Southeast Asia, South America, Europe, and the U.S.

Industry/Entity Type

Veterinary test kit for dogs & cats

Colors
0054AA
0677BA
7BADD7
CADEEF
E8F1F8
0094D4
00A9DD
6FCCEA
C7EBF8
E9F6FB
00AB8E
00BBA5
67D7C9
C6EFE9
E9F9F6
59FF00
82FF00
B8FF75
E3FFCB
F4FFEA
F0912C
F2A743
F7CA91
FBE8D2
FDF5EE
EE7325
F08F49
F5BC92
FAE3D3
FDF4ED

Requirements
Nice to have
• Appealing Box Appearance with professional

```html
<!DOCTYPE html>
<html lang="en">
<head>
<meta charset="utf-8">
<title>PAWSURE Rapid Test Kit – Box Panels</title>
<link rel="stylesheet" href="https://fonts.googleapis.com/css2?family=Montserrat:ital,wght@0,400;0,500;0,600;0,700;0,800;1,600;1,700&display=swap">
<style>
:root{
  --stage:#808080;
  --orange:#F15A24;
  --orange-light:#F5875A;
  --orange-pale:#FAD3BF;
  --steel:#BDCCD6;
  --white:#FFFFFF;
  --ink:#1A1A1A;
  --grey-text:#A9B8C2;
}
*{margin:0;padding:0;box-sizing:border-box}
html,body{width:1200px;height:2667px;overflow:hidden}
body{background:var(--stage);font-family:"Montserrat",sans-serif;position:relative;color:var(--white)}
.panel{position:absolute;overflow:hidden}
.band{position:absolute;left:0;right:0;height:20px;background:var(--steel)}

/* top lid */
.lid{left:25px;top:1010px;width:675px;height:525px;background:var(--orange)}
.lid .photo{position:absolute;left:0;top:0;width:675px;height:505px;
  background:radial-gradient(ellipse at 70% 35%,var(--orange-pale) 0%,var(--orange-light) 40%,var(--orange) 80%),var(--orange)}
.lid .band{top:505px}
.lid .brand{position:absolute;left:180px;top:405px;font-size:74px}

.brand{font-weight:800;letter-spacing:-1px;line-height:1;color:var(--white);font-family:"Montserrat",sans-serif;white-space:nowrap}

/* front panels */
.front{left:25px;width:675px;height:522px;background:var(--orange)}
.front.en{top:1563px}
.front.es{top:2115px}
.front .band{top:0}
.front .brand{position:absolute;left:50px;top:65px;font-size:60px}
.front .subtitle{position:absolute;left:50px;top:130px;width:338px;font-size:17px;font-weight:600;line-height:1.2;letter-spacing:-0.2px;white-space:nowrap}
.front .rule{position:absolute;left:396px;right:0;top:140px;height:4px;background:var(--white)}
.front .tagline{position:absolute;left:50px;font-size:22px;font-style:italic;font-weight:600}
.en .tagline{top:170px}
.es .tagline{top:192px}
.front .contents-title{position:absolute;left:50px;font-size:22px;font-weight:800}
.en .contents-title{top:224px}
.es .contents-title{top:240px}
.contents-list{position:absolute;left:50px;list-style:none;font-size:15.5px;font-weight:600;line-height:18px}
.en .contents-list{top:268px}
.es .contents-list{top:284px}
.contents-list li{display:flex;align-items:center;gap:6px}
.num{display:inline-flex;width:14px;height:14px;border-radius:50%;background:var(--white);color:var(--orange);font-size:10px;font-weight:800;align-items:center;justify-content:center}
.storage{position:absolute;left:52px;font-size:15.5px;font-weight:600}
.en .storage{top:352px}
.es .storage{top:368px}
.count{position:absolute;left:540px;top:335px;width:72px;text-align:center;line-height:1}
.count .n{font-size:58px;font-weight:800;letter-spacing:-3px;display:block}
.count .l1{font-size:13px;font-weight:800;display:block;margin-top:-2px}
.count .l2{font-size:9.5px;font-weight:600;display:block}
.icons{position:absolute;left:48px;top:415px;width:620px;height:70px}

/* side panels */
.side-steel{left:720px;top:1563px;width:453px;height:522px;background:var(--steel)}
.side-steel .brand{position:absolute;left:50px;top:62px;font-size:58px}
.side-steel .tagline{position:absolute;left:50px;top:120px;font-size:22px;font-style:italic;font-weight:600}

.side-white{left:723px;top:2115px;width:450px;height:522px;background:var(--white);color:var(--ink)}
.side-white .brand{position:absolute;left:49px;top:70px;font-size:56px;color:var(--orange)}
.side-white .kit{position:absolute;left:49px;top:125px;font-size:23px;font-weight:600;color:var(--grey-text)}
.side-white .rule{position:absolute;left:222px;right:0;top:140px;height:4px;background:var(--steel)}
.feature{position:absolute;width:178px}
.col-en{left:49px}
.col-es{left:222px;width:190px}
.row1{top:162px}
.row2{top:220px}
.row3{top:276px}
.row4{top:360px}
.feature h3{font-size:12px;font-weight:700;color:var(--orange);line-height:15px;text-transform:uppercase}
.feature p{font-size:9.5px;font-weight:600;line-height:13px;color:var(--ink)}
.maker{position:absolute;left:49px;top:462px;font-size:15px;font-style:italic;font-weight:700;color:var(--ink)}
.maker-tag{position:absolute;left:49px;top:481px;font-size:9.5px;font-style:italic;font-weight:600;color:var(--orange)}
</style>
</head>
<body>

<svg width="0" height="0" style="position:absolute" aria-hidden="true">
  <defs>
    <symbol id="icon-row" viewBox="0 0 620 70">
      <g fill="none" stroke="#fff" stroke-width="2">
        <rect x="1" y="8" width="80" height="50"/>
        <path d="M146 14v38" stroke-width="3"/>
        <circle cx="146" cy="56" r="5" fill="#fff"/>
        <path d="M132 58l14 -4M146 14l14 -6"/>
        <circle cx="254" cy="14" r="6"/>
        <path d="M254 1v5M254 22v5M241 14h5M262 14h5M245 5l3 3M260 20l3 3M263 5l-3 3M248 20l-3 3"/>
        <path d="M206 44l26 -18 26 18"/>
        <path d="M290 22c10 -8 24 -8 34 0v44c-10 -8 -24 -8 -34 0zM324 22c10 -8 24 -8 34 0v44c-10 -8 -24 -8 -34 0z"/>
        <circle cx="446" cy="40" r="26"/>
        <path d="M428 22l36 36"/>
        <path d="M524 30l28 -12 30 12v26l-30 12 -28 -12z M524 30l30 12 28 -12 M554 42v26 M524 30l-6 12 30 12"/>
      </g>
      <text x="41" y="44" fill="#fff" font-family="Montserrat,sans-serif" font-size="30" font-weight="600" text-anchor="middle">IVD</text>
      <text x="102" y="62" fill="#fff" font-family="Montserrat,sans-serif" font-size="14" font-weight="600">2°C</text>
      <text x="160" y="16" fill="#fff" font-family="Montserrat,sans-serif" font-size="14" font-weight="600">30°C</text>
      <rect x="222" y="46" width="14" height="14" fill="#fff"/>
      <rect x="350" y="36" width="6" height="20" fill="#fff"/>
      <circle cx="353" cy="28" r="3" fill="#fff"/>
      <text x="446" y="54" fill="#fff" font-family="Montserrat,sans-serif" font-size="36" font-weight="400" text-anchor="middle">2</text>
    </symbol>
  </defs>
</svg>

<!-- Lid -->
<section class="panel lid">
  <div class="photo" role="img" aria-label="Orange duotone photograph of a dog and a cat side by side"></div>
  <div class="brand">PAWSURE</div>
  <div class="band"></div>
</section>

<!-- Front panel, English -->
<section class="panel front en">
  <div class="band"></div>
  <div class="brand">PAWSURE</div>
  <p class="subtitle">Pet Rapid Test Kit for Dogs &amp; Cats</p>
  <div class="rule"></div>
  <p class="tagline">Loved by Pets, Trusted by Vets</p>
  <h2 class="contents-title">CONTENTS:</h2>
  <ol class="contents-list">
    <li><span class="num">1</span>Test Kits(cassette, disposable dropper, desiccant).</li>
    <li><span class="num">2</span>Assay buffer.</li>
    <li><span class="num">3</span>Sterile swabs.</li>
    <li><span class="num">4</span>Instruction manual.</li>
  </ol>
  <p class="storage">Store at 2~30°C, avoid direct sunlight.</p>
  <div class="count"><span class="n">10</span><span class="l1">TESTS</span><span class="l2">PER BOX</span></div>
  <svg class="icons" role="img" aria-label="IVD, storage temperature, keep away from sunlight, read instructions, single use, box symbols"><use href="#icon-row"/></svg>
</section>

<!-- Side panel, steel -->
<section class="panel side-steel">
  <div class="brand">PAWSURE</div>
  <p class="tagline">Loved by Pets, Trusted by Vets</p>
</section>

<!-- Front panel, Spanish -->
<section class="panel front es">
  <div class="band"></div>
  <div class="brand">PAWSURE</div>
  <p class="subtitle">Kit De Prueba Rápida Para Mascotas<br>(Perros Y Gatos)</p>
  <div class="rule"></div>
  <p class="tagline">Querido por las mascotas, confiado por veterinarios</p>
  <h2 class="contents-title">CONTENTS:</h2>
  <ol class="contents-list">
    <li><span class="num">1</span>Kits de prueba (cassette, gotero desechable, desecante).</li>
    <li><span class="num">2</span>Buffer de ensayo.</li>
    <li><span class="num">3</span>Hisopos estériles.</li>
    <li><span class="num">4</span>Manual de instrucciones.</li>
  </ol>
  <p class="storage">Almacenamiento: 2~30°C.</p>
  <div class="count"><span class="n">10</span><span class="l1" style="font-size:10px">PRUEBAS</span><span class="l2">POR CAJA</span></div>
  <svg class="icons" role="img" aria-label="IVD, storage temperature, keep away from sunlight, read instructions, single use, box symbols"><use href="#icon-row"/></svg>
</section>

<!-- Side panel, white -->
<section class="panel side-white">
  <div class="brand">PAWSURE</div>
  <p class="kit">Rapid Test Kit</p>
  <div class="rule"></div>

  <div class="feature col-en row1"><h3>Simple &amp; Convenient</h3><p>No professional skills required,<br>Simple enough for home use.</p></div>
  <div class="feature col-en row2"><h3>Fast &amp; Efficient</h3><p>Digital results in &lt; 10 minutes<br>– from start to completion.</p></div>
  <div class="feature col-en row3"><h3>Accurate &amp; Reliable</h3><p>Quick and trustworthy pet<br>health results using advanced<br>lateral flow biotech, trusted by<br>vet clinics worldwide.</p></div>
  <div class="feature col-en row4"><h3>Supports Screening<br>of Multiple Diseases</h3><p>Helping pet owners detect<br>issues early.</p></div>

  <div class="feature col-es row1"><h3>Fácil y Práctico</h3><p>Sin capacitación previa, suficiente-<br>mente simple para uso en casa.</p></div>
  <div class="feature col-es row2"><h3>Rápido y Eficiente</h3><p>Resultados digitales en &lt;10 minutos<br>desde inicio hasta resultado final.</p></div>
  <div class="feature col-es row3"><h3>Preciso y Fiable</h3><p>Resultados rápidos y confiables<br>con tecnología de inmunocroma-<br>tografía avanzada, validado por<br>clínicas veterinarias a nivel global.</p></div>
  <div class="feature col-es row4"><h3>Detección Multien<br>fermedades</h3><p>Evalúa múltiples patologías<br>simultáneamente. Ayudar a los<br>dueños de mascotas a detectar<br>problemas a tiempo.</p></div>

  <p class="maker">MADE by VETNORA™</p>
  <p class="maker-tag">Loved by Pets, Trusted by Vets</p>
</section>

</body>
</html>
```